The Molar Ledger (Cover Design for Ebook)

I need a cool and exciting eBook cover for my new book, launching very soon!
I want it to stand out and appeal to young professionals with big dreams.
It should be dramatic and bold and avoid cliche or generic photos. Simple design will work as long as it relates to the message of the book. The content will provide ten years of experience from working in the field and achieving success.
Title: The Molar Ledger (at the top)
(Subheading Updated) The secrets to money, motivation and success they don’t teach you in dental school
OR The secrets to success they don't teach you in dental school.
OR The secrets to money, motivation and success
(smaller under title)
Author Updated: Dr K Fenwick (place at the bottom)
Updates

Target Market(s)

Ambitious young dentists
See instagram www.snapverse.net/themolarledger for a sense of the style that I think could work.

Font styles to use
Serif
Sans Serif

Colors

Designer to choose colors to be used in the design.

Requirements
Must have
• Eye catching and cool.
• Show the benefits of success. Money, freedom, luxury
• Clear title and subheading
Nice to have
• Subtle dental reference
• dimensions 1600x2400
Should not have
• Boring photos of dentist/patients, dental clinic, teeth etc,

```html
<!DOCTYPE html>
<html lang="en">
<head>
<meta charset="utf-8">
<title>The Molar Ledger — Cover</title>
<link rel="stylesheet" href="https://fonts.googleapis.com/css2?family=Cinzel:wght@400;500&family=Questrial&display=swap">
<style>
  :root {
    --sea-deep: #0b67a6;
    --sea-mid: #2bb9a9;
    --gold-light: #fff27a;
    --gold: #f2c200;
    --gold-dark: #9a6a00;
    --ink-subtitle: #12455e;
    --crystal-light: #d9d2ff;
    --crystal: #a88cf0;
    --crystal-deep: #7a55e0;
  }
  html, body {
    margin: 0;
    padding: 0;
    overflow: hidden;
  }
  .cover {
    position: relative;
    width: 800px;
    height: 1200px;
    overflow: hidden;
    background: linear-gradient(180deg, var(--sea-deep) 0%, var(--sea-mid) 50%, var(--sea-deep) 100%);
  }
  .gold-type {
    position: absolute;
    left: 0;
    width: 100%;
    margin: 0;
    text-align: center;
    font-family: "Cinzel", serif;
    font-weight: 400;
    line-height: 1;
    background: linear-gradient(180deg, var(--gold-light) 0%, var(--gold) 45%, var(--gold-dark) 100%);
    -webkit-background-clip: text;
    background-clip: text;
    color: transparent;
    filter: drop-shadow(1px 2px 0 rgba(60, 35, 0, 0.55));
  }
  .title-article {
    top: 48px;
    font-size: 78px;
    letter-spacing: 4px;
  }
  .title-main {
    top: 148px;
    font-size: 136px;
    letter-spacing: 2px;
  }
  .title-second {
    top: 298px;
    font-size: 136px;
    letter-spacing: 2px;
  }
  .subtitle {
    position: absolute;
    top: 438px;
    left: 0;
    width: 100%;
    margin: 0;
    text-align: center;
    font-family: "Questrial", sans-serif;
    font-size: 30px;
    color: var(--ink-subtitle);
  }
  .crystal-tooth {
    position: absolute;
    left: 172px;
    top: 488px;
    width: 460px;
    height: 440px;
    border-radius: 40% 30% 30% 40%;
    background: radial-gradient(ellipse at 30% 50%, var(--crystal-light) 0%, var(--crystal) 40%, rgba(122, 85, 224, 0.25) 70%, rgba(122, 85, 224, 0) 100%);
  }
  .author {
    top: 1025px;
    font-size: 88px;
    letter-spacing: 2px;
  }
</style>
</head>
<body>
  <main class="cover">
    <h1 class="book-title">
      <span class="gold-type title-article">THE</span>
      <span class="gold-type title-main">MOLAR</span>
      <span class="gold-type title-second">LEDGER</span>
    </h1>
    <p class="subtitle">The Secrets to Money, Motivation and Success</p>
    <div class="crystal-tooth" role="img" aria-label="Faceted violet crystal tooth dissolving into drifting triangular shards"></div>
    <p class="gold-type author">KIT FENWICK</p>
  </main>
</body>
</html>
```